Supplement Company Needs a Protein Powder Pouch Design

We are looking for a modern and fresh design for our 500g pouches of protein powder as our current design is not eye catching or exciting enough.

This new design will be printed on both sides of a 178mm x 280mm x 101mm pouch.

We have 4 flavours. These are Banana Ice Cream, Chocolate Deluxe, Strawberries & Cream and Vanilla Ice Cream.

Industry/Entity Type

Supplement

Requirements
Must have
• Attractive and eye catching front and space for all the nutritional information and ingredients on the back.

Must clearly state 'food supplement' somewhere on the front of the pouch.
Nice to have
• Our logo is attached.
Should not have
• No health claims as these are not allowed in the UK

```html
<!DOCTYPE html>
<html lang="en">
<head>
<meta charset="UTF-8">
<title>Plume Supplements – Protein Powder Chocolate Pouch</title>
<link rel="stylesheet" href="https://fonts.googleapis.com/css2?family=Oswald:wght@400;500;600&family=Montserrat:wght@700&family=Yellowtail&family=Cookie&display=swap">
<style>
  :root {
    --stage: #f2f2f2;
    --pouch: #121212;
    --pouch-edge: #0a0a0a;
    --ink: #f1efec;
    --cocoa-dark: #7a4126;
    --cocoa: #9c5a34;
    --cocoa-light: #b87042;
    --label-bg: #ffffff;
    --label-ink: #1a1a1a;
  }
  * { box-sizing: border-box; margin: 0; padding: 0; }
  html, body {
    width: 1200px; height: 1200px; overflow: hidden;
    background: var(--stage);
  }
  .pouch-front {
    position: absolute; left: 231px; top: 20px;
    width: 738px; height: 1160px;
    background: linear-gradient(180deg, var(--pouch) 0%, var(--pouch-edge) 100%);
    color: var(--ink);
    font-family: 'Oswald', sans-serif;
    overflow: hidden;
  }
  .center { position: absolute; left: 0; width: 100%; text-align: center; }

  .brand-name {
    top: 196px;
    font-family: 'Montserrat', sans-serif; font-weight: 700;
    font-size: 86px; letter-spacing: -2px; line-height: 1;
  }
  .brand-sub {
    top: 306px;
    font-family: 'Montserrat', sans-serif; font-weight: 700;
    font-size: 17px; letter-spacing: 13px; padding-left: 13px;
  }
  .category {
    top: 418px; font-size: 42px; font-weight: 500; letter-spacing: 1px;
  }
  .product-title {
    top: 486px; font-size: 162px; font-weight: 500; line-height: 1;
    letter-spacing: 2px;
  }
  .product-subtitle {
    top: 650px; font-size: 96px; font-weight: 500; line-height: 1;
  }
  .leaf-ornament {
    position: absolute; left: 86px; top: 688px; width: 92px; height: 72px;
    background: linear-gradient(135deg, var(--cocoa-dark), #4d2a19);
    border-radius: 40px 4px 40px 4px; opacity: .8;
  }
  .flavour-band {
    position: absolute; left: 0; top: 792px; width: 100%; height: 66px;
    background: linear-gradient(90deg, var(--cocoa-dark), var(--cocoa) 50%, var(--cocoa-light));
  }
  .flavour-art {
    position: absolute; left: 78px; top: 784px; width: 164px; height: 94px;
    background: linear-gradient(160deg, #8a4e2e, #5d3320);
    border-radius: 6px;
  }
  .flavour-name {
    position: absolute; left: 246px; top: 782px;
    font-family: 'Yellowtail', cursive; font-size: 82px; line-height: 1;
  }
  .flavour-note {
    position: absolute; left: 250px; width: 260px; top: 868px;
    text-align: center; font-size: 30px; font-weight: 500;
  }
  .tagline {
    position: absolute; left: 202px; width: 320px; top: 922px;
    text-align: center; font-family: 'Cookie', cursive; font-size: 40px;
    line-height: 1.05; padding-bottom: 2px;
    border-bottom: 1.5px dashed var(--ink);
  }
  .nutrition-row {
    position: absolute; left: 0; width: 100%; top: 990px;
    display: flex; justify-content: center; gap: 16px; padding-left: 0;
  }
  .nutrition-badge {
    width: 68px; height: 72px; border: 1.5px solid var(--ink); border-radius: 12px;
    text-align: center; padding-top: 7px;
  }
  .nutrition-badge .label { font-size: 14px; font-weight: 500; display: block; line-height: 1.1; }
  .nutrition-badge .value { font-size: 27px; font-weight: 600; line-height: 1.3; }
  .nutrition-badge .unit { font-size: 13px; font-weight: 500; }
  .footer-rule {
    position: absolute; left: 0; width: 100%; top: 1084px; height: 2px; background: var(--ink);
  }
  .footer-band {
    position: absolute; left: 0; width: 100%; top: 1094px; height: 48px;
    background: linear-gradient(90deg, var(--cocoa-dark), var(--cocoa) 50%, var(--cocoa-light));
  }
  .net-weight {
    position: absolute; left: 321px; top: 1098px; width: 96px; height: 42px;
    background: var(--label-bg); color: var(--label-ink);
    border: 1px solid #555;
    font-family: Arial, Helvetica, sans-serif; font-size: 14px; line-height: 1.2;
    text-align: center; padding-top: 3px;
  }
</style>
</head>
<body>
  <main class="pouch-front">
    <div class="center brand-name">PLUME</div>
    <div class="center brand-sub">SUPPLEMENTS</div>

    <div class="center category">-- FOOD SUPPLEMENT --</div>
    <h1 class="center product-title">PROTEIN</h1>
    <div class="center product-subtitle">POWDER</div>

    <div class="leaf-ornament" role="img" aria-label="Decorative cocoa leaves"></div>

    <div class="flavour-band"></div>
    <div class="flavour-art" role="img" aria-label="Sketch of broken chocolate bar pieces"></div>
    <div class="flavour-name">Chocolate</div>
    <div class="flavour-note">DELUXE FLAVOUR</div>

    <div class="tagline">Low calorie protein shake</div>

    <div class="nutrition-row">
      <div class="nutrition-badge"><span class="label">PROTEIN</span><span class="value">21</span><span class="unit">g</span></div>
      <div class="nutrition-badge"><span class="label">ENERGY</span><span class="value">489</span><span class="unit">kj</span></div>
      <div class="nutrition-badge"><span class="label">CARBS</span><span class="value">4.2</span><span class="unit">g</span></div>
    </div>

    <div class="footer-rule"></div>
    <div class="footer-band"></div>
    <div class="net-weight">NET.WT<br>500 g</div>
  </main>
</body>
</html>
```